Flyer für Selbstbedienungshütte
Zielgruppe
Selbstbedienungshütte 'Lindenruh', Radfahrer, Wanderer oder Leute die einfach nur die Aussicht genießen, relaxen oder sich Stärken wollen.
Koordinaten der Hütte: 46.5281937, 14.2917605
Vorschläge für Stock-Bildern sind gerne auch erlaubt.
Aufgabenstellung
Die Landschaft um die Selbstbedienungshütte befindet sich noch im Aufbau. Bitte in einen Format liefern sodaß Fotos getauscht werden können.
Auf der Rückseite des Flyers wäre eine Karte mit den Koordinaten zur Hütte super. Zusätzlich sollen dort später auch ein paar Fotos von der Hütte und der Umgebung platzfinden. Ev. auch noch die genaue Adresse.

```html
<!DOCTYPE html>
<html lang="de">
<head>
<meta charset="utf-8">
<title>Sonnleit – Flyer Selbstbedienungshütte Lindenruh</title>
<link href="https://fonts.googleapis.com/css2?family=Poppins:wght@400;600;700&family=Oswald:wght@600&family=Merriweather:wght@700&family=Kaushan+Script&display=swap" rel="stylesheet">
<style>
  :root {
    --stage: #8aa7a6;
    --wine-red: #b01c22;
    --ink: #111111;
    --paper: #ffffff;
    --sky-top: #a9d1ee;
    --sky-mid: #d9ebf7;
    --sky-low: #f3f8fc;
    --meadow: #5f8a3a;
    --forest: #4a7432;
  }
  * { box-sizing: border-box; margin: 0; padding: 0; }
  html, body { width: 1200px; height: 1117px; overflow: hidden; }
  body { background: var(--stage); position: relative; font-family: "Poppins", sans-serif; }

  .flyer {
    position: absolute; left: 220px; top: 21px; width: 760px; height: 1075px;
    background: var(--paper); overflow: hidden;
  }
  .sky {
    position: absolute; left: 0; top: 0; width: 760px; height: 860px;
    background: linear-gradient(180deg, var(--sky-top) 0%, var(--sky-mid) 50%, var(--sky-low) 100%);
  }
  .landscape {
    position: absolute; left: 0; top: 850px; width: 760px; height: 205px;
    background: linear-gradient(180deg, var(--sky-low) 0%, #a9b9a0 22%, var(--forest) 50%, var(--meadow) 100%);
  }

  .brand {
    position: absolute; left: 40px; top: 150px;
    display: flex; align-items: center; gap: 20px;
  }
  .brand-name {
    font-family: "Poppins", sans-serif; font-weight: 700;
    font-size: 132px; line-height: 1; color: var(--wine-red); letter-spacing: -2px;
  }
  .brand-dot { width: 44px; height: 44px; border-radius: 50%; background: #2a2326; margin-top: -70px; }

  .welcome {
    position: absolute; right: 50px; top: 330px; text-align: right;
    font-family: "Kaushan Script", cursive; font-weight: 400; line-height: 1;
  }
  .welcome .line1 { display: block; font-size: 60px; color: var(--ink); }
  .welcome .line2 { display: block; font-size: 58px; color: var(--wine-red); margin-top: 2px; }

  .photo-circle {
    position: absolute; border-radius: 50%; border: 9px solid var(--paper);
    box-shadow: 0 2px 8px rgba(0,0,0,.12);
  }
  .photo-terrace {
    left: 28px; top: 406px; width: 274px; height: 274px;
    background: linear-gradient(180deg, #cfd9e0 0%, #6f8e50 40%, #c48a3a 70%, #a56a2a 100%);
  }
  .photo-vineyard {
    left: 258px; top: 458px; width: 224px; height: 224px;
    background: linear-gradient(180deg, #8fb6d9 0%, #b7c6d2 35%, #7a8a3a 60%, #9d8a2f 100%);
  }

  .location { position: absolute; left: 500px; top: 470px; }
  .location-label {
    display: flex; align-items: center; gap: 6px;
    font-family: "Merriweather", serif; font-weight: 700; font-size: 13.5px; color: var(--ink);
  }
  .location-coords {
    margin: 8px 0 0 14px; font-family: "Poppins", sans-serif; font-weight: 700;
    font-size: 32px; line-height: 1.08; color: var(--ink);
  }
  .location-web {
    display: inline-block; margin: 14px 0 0 17px; padding: 5px 13px;
    background: var(--wine-red); color: var(--paper); border-radius: 7px;
    font-family: "Merriweather", serif; font-weight: 700; font-size: 15px;
  }

  .claim {
    position: absolute; left: 52px; top: 692px;
    font-family: "Oswald", sans-serif; font-weight: 600; font-size: 54px; line-height: 1;
    display: flex; align-items: center; gap: 14px; letter-spacing: .5px;
  }
  .claim .red { color: var(--wine-red); }
  .claim .black { color: var(--ink); }
  .claim .dots { color: var(--wine-red); font-size: 30px; letter-spacing: 2px; }

  .intro {
    position: absolute; left: 52px; top: 756px; width: 535px;
    font-size: 12.6px; line-height: 1.3; color: var(--ink);
  }
  .intro p + p { margin-top: 9px; }

  .partner-card {
    position: absolute; left: 480px; top: 963px; width: 280px; height: 92px;
    background: var(--paper); border-top-left-radius: 46px;
    display: flex; align-items: center; justify-content: center; gap: 10px; padding-top: 8px;
  }
  .partner-name { font-family: "Poppins", sans-serif; font-weight: 600; font-size: 30px; color: var(--ink); }
  .partner-mark { width: 12px; height: 12px; border-radius: 50%; background: var(--wine-red); }
</style>
</head>
<body>
  <main class="flyer">
    <div class="sky" role="img" aria-label="Foto: blauer Himmel mit weißen Wolken"></div>
    <div class="landscape" role="img" aria-label="Foto: Selbstbedienungshütte vor Bergpanorama mit Wiese und Bäumen"></div>

    <div class="brand">
      <span class="brand-name">Sonnleit</span>
      <span class="brand-dot"></span>
    </div>

    <h1 class="welcome">
      <span class="line1">Herzlich</span>
      <span class="line2">willkommen!</span>
    </h1>

    <div class="photo-circle photo-terrace" role="img" aria-label="Foto: Holztisch und Liegestuhl mit Blumenvase vor Weinlandschaft"></div>
    <div class="photo-circle photo-vineyard" role="img" aria-label="Foto: Weingarten mit Pappel und Rose im Vordergrund"></div>

    <div class="location">
      <div class="location-label">
        <svg width="11" height="15" viewBox="0 0 12 16" aria-hidden="true"><path d="M6 0C2.7 0 0 2.6 0 5.9 0 10.3 6 16 6 16s6-5.7 6-10.1C12 2.6 9.3 0 6 0zm0 8.3A2.4 2.4 0 1 1 6 3.5a2.4 2.4 0 0 1 0 4.8z" fill="#b01c22"/></svg>
        Koordinaten der Hütte:
      </div>
      <div class="location-coords">46.5281937,<br>14.2917605</div>
      <div class="location-web">sonnleit-wein.at</div>
    </div>

    <h2 class="claim">
      <span class="red">WEIN</span><span class="dots">•••</span>
      <span class="black">GENUSS</span><span class="dots">•••</span>
      <span class="red">LEBEN</span>
    </h2>

    <div class="intro">
      <p>Faszinierendes Naturpanorama – hervorragende klimatische Bedingungen und konsequente Qualitätsphilosophie – das macht uns besonders!</p>
      <p>Besuchen Sie uns direkt am Weinhof oder gustieren Sie gemütlich von zu Hause durch unseren Online Shop. Wir freuen uns!</p>
    </div>

    <div class="partner-card">
      <span class="partner-name">Lindenruh</span>
      <span class="partner-mark"></span>
    </div>
  </main>
</body>
</html>
```